Stem Cell Injections

We are making a brochure for injecting stem cells into joints tendons and muscles to repair chronic and acute injuries.
i need a six page brochure
kelvawind.com name of website
web sites that have similar feel are
http://www.lumatorv.com/quandrelo-procedures/
http://www.bravitoque.com/stemcelltreatments/rheumatoidarthritisstemcelltreatment.html
http://www.bravitoque.com/stemcellvideos/orthopedicstemcelltherapy.html
http://thewillowbyclinic.com/bone-marrow-cell-concentrate-platelet-rich-plasma.asp
Requirements
Must have
- Graphics of injections into joints, tendons and muscle showing injections
for ideas please google image search "joint injections"
Nice to have
- we need personal bios of both doctors that do the procedures.
Should not have
- should look very modern not classic or old

```html
<!DOCTYPE html>
<html lang="en">
<head>
<meta charset="utf-8">
<title>Platelet-Rich Plasma and BMCC Brochure</title>
<link href="https://fonts.googleapis.com/css2?family=Roboto:ital,wght@0,400;0,700;1,700&family=Roboto+Condensed:wght@400;700&display=swap" rel="stylesheet">
<style>
  :root {
    --page-bg: #e9e9e9;
    --paper: #ffffff;
    --teal: #2f7d72;
    --teal-head: #2a8a86;
    --teal-light: #5cc3c0;
    --navy: #1c2466;
    --navy-deep: #1a2270;
    --ink: #2b2b33;
  }
  * { box-sizing: border-box; margin: 0; padding: 0; }
  html, body { width: 1200px; height: 686px; overflow: hidden; background: var(--page-bg); }
  body { font-family: "Roboto Condensed", Arial, sans-serif; color: var(--ink); }

  .spread {
    position: absolute; left: 180px; top: 16px;
    width: 841px; height: 654px; background: var(--paper);
    box-shadow: 0 2px 10px rgba(0,0,0,.18);
    overflow: hidden;
  }
  .spread-shapes { position: absolute; inset: 0; width: 100%; height: 100%; }

  /* brand */
  .brand {
    position: absolute; left: 592px; top: 38px;
    display: flex; align-items: center; gap: 10px;
  }
  .brand-mark { width: 24px; height: 24px; background: var(--navy); }
  .brand-name {
    font-family: "Roboto Condensed", Arial, sans-serif;
    font-weight: 700; font-size: 18px; line-height: 1.1;
    color: var(--teal);
  }

  /* left panel */
  .panel-info { position: absolute; left: 14px; top: 180px; width: 256px; }
  .info-title {
    font-weight: 700; font-size: 11.5px; line-height: 1.2; color: var(--navy);
    text-align: justify; text-align-last: left;
  }
  .info-heading {
    font-weight: 700; font-size: 12px; color: var(--teal-head);
    margin: 8px 0 7px;
  }
  .info-text {
    font-size: 8.6px; line-height: 1.4; text-align: justify; color: #333;
  }
  .panel-bmcc { position: absolute; left: 14px; top: 520px; width: 256px; }
  .panel-bmcc .info-heading { margin-top: 0; }
  .panel-bmcc .info-text { font-size: 8.4px; line-height: 1.36; }

  /* middle panel */
  .panel-conditions { position: absolute; left: 296px; top: 178px; width: 252px; color: #fff; }
  .conditions-title {
    font-weight: 700; font-size: 15.5px; line-height: 1.2; color: var(--teal-light);
    width: 240px;
  }
  .conditions-cols { display: flex; justify-content: space-between; margin-top: 10px; position: relative; }
  .conditions-cols::after {
    content: ""; position: absolute; left: 134px; top: 4px; width: 1px; height: 250px;
    background: rgba(255,255,255,.55);
  }
  .condition-list {
    list-style: none;
    font-size: 10px; line-height: 1.3;
  }
  .condition-list li.gap { margin-top: 13px; }
  .col-left { width: 118px; text-align: justify; text-align-last: left; }
  .col-right { width: 110px; text-align: right; }

  .contact { position: absolute; left: 352px; top: 538px; color: var(--navy-deep); }
  .contact-title { font-weight: 700; font-size: 19px; margin-bottom: 6px; }
  .contact-line {
    display: flex; align-items: center; gap: 5px;
    font-weight: 700; font-size: 15px; color: #fff; margin-bottom: 5px;
  }
  .contact-line svg { width: 13px; height: 13px; fill: var(--navy-deep); }

  /* cover panel */
  .cover-title {
    position: absolute; left: 566px; top: 556px; width: 270px;
    font-family: "Roboto", Arial, sans-serif; font-style: italic;
    font-weight: 700; font-size: 21px; line-height: 1.45;
    color: var(--navy); text-align: center;
  }
</style>
</head>
<body>
<main class="spread">
  <svg class="spread-shapes" viewBox="0 0 841 654" preserveAspectRatio="none" aria-hidden="true">
    <defs>
      <clipPath id="topStrip"><polygon points="0,0 559,0 559,106 283,158 0,167"/></clipPath>
      <linearGradient id="skinA" x1="0" y1="0" x2="1" y2="1">
        <stop offset="0" stop-color="#fbf3ee"/><stop offset=".5" stop-color="#e3bfa8"/><stop offset="1" stop-color="#f6e6dc"/>
      </linearGradient>
      <linearGradient id="skinB" x1="0" y1="1" x2="1" y2="0">
        <stop offset="0" stop-color="#f4e2d6"/><stop offset=".55" stop-color="#dcb197"/><stop offset="1" stop-color="#fbf4ef"/>
      </linearGradient>
      <linearGradient id="coverPhoto" x1="0" y1="0" x2="1" y2="1">
        <stop offset="0" stop-color="#fdf8f5"/><stop offset=".45" stop-color="#e8c3ab"/><stop offset=".75" stop-color="#f1d9c9"/><stop offset="1" stop-color="#fbf3ee"/>
      </linearGradient>
      <linearGradient id="clinicPhoto" x1="0" y1="0" x2="1" y2="1">
        <stop offset="0" stop-color="#e7ecf1"/><stop offset=".35" stop-color="#8b96a3"/><stop offset=".7" stop-color="#2e3947"/><stop offset="1" stop-color="#1b2430"/>
      </linearGradient>
      <linearGradient id="navyPanel" x1="0" y1="0" x2="1" y2="1">
        <stop offset="0" stop-color="#1f2a78"/><stop offset="1" stop-color="#3d2d8f"/>
      </linearGradient>
    </defs>

    <g clip-path="url(#topStrip)">
      <rect x="0" y="0" width="160" height="170" fill="url(#skinA)" role="img" aria-label="Photo of an injection into a hand"/>
      <rect x="166" y="0" width="216" height="170" fill="url(#skinB)" role="img" aria-label="Photo of an injection into a shoulder"/>
      <rect x="388" y="0" width="171" height="170" fill="url(#skinA)" role="img" aria-label="Photo of an injection into an elbow"/>
    </g>

    <polygon points="0,166 283,157 559,105 841,160 841,176 559,121 283,172 0,181" fill="var(--teal)"/>
    <polygon points="283,172 559,121 559,468 283,511" fill="url(#navyPanel)"/>
    <polygon points="559,121 841,176 841,490 559,468" fill="url(#coverPhoto)" role="img" aria-label="Photo of hands giving an injection into a knee joint"/>
    <polygon points="283,511 559,468 841,490 841,654 283,654" fill="var(--teal)"/>
    <line x1="559" y1="466" x2="841" y2="488" stroke="var(--navy)" stroke-width="6"/>
    <rect x="0" y="404" width="282" height="107" fill="url(#clinicPhoto)" role="img" aria-label="Photo of a clinician preparing an ankle injection"/>
    <line x1="283" y1="172" x2="283" y2="654" stroke="var(--navy)" stroke-width="2"/>
    <line x1="0" y1="511" x2="283" y2="511" stroke="var(--navy)" stroke-width="2"/>
  </svg>

  <div class="brand">
    <span class="brand-mark"></span>
    <span class="brand-name">Kestrel Joint Care<br>Group, P.C.</span>
  </div>

  <section class="panel-info">
    <h1 class="info-title">Platelet-Rich Plasma and BMCC (Bone Marrow Cell Concentrate) Explained:</h1>
    <h2 class="info-heading">What is Platelet-Rich Plasma (PRP)?</h2>
    <p class="info-text">Platelet-rich plasma or PRP is an “autologous blood therapy” that uses a patient’s own blood components to stimulate a healing response in damaged tissues. In response to an injury or tissue damage, your body naturally recruits platelets and white blood cells from the blood to initiate a healing response. Under normal conditions, platelets store numerous growth factors which are released in response to signals from the injured tissue. Modern technology allows us to concentrate platelets and white blood cells from your blood, and induce this growth factor release as we inject the solution directly into injured tissue, simulating this same healing response in a more powerful form. By enhancing the body’s natural healing capacity, the treatment may lead to a more rapid, more efficient, and more thorough restoration of the tissue to a healthy state.</p>
  </section>

  <section class="panel-bmcc">
    <h2 class="info-heading">What is Bone Marrow Cell Concentrate (BMCC)?</h2>
    <p class="info-text">It is well established that a significant population of our bodies’ stem cells are contained within our bone marrow. By harvesting blood and tissue from the bone marrow space of the hip, an injectable product can be produced by concentrating platelets and cells withdrawn through a simple outpatient needle aspiration procedure, done with local anesthetic and light sedation. BMCC contains all of the growth and healing factors in PRP, along with concentrated “pluripotent” or stem-like cells which further contribute to the regenerative process.</p>
  </section>

  <section class="panel-conditions">
    <h2 class="conditions-title">What conditions can be treated with PRP and BMCC?</h2>
    <div class="conditions-cols">
      <ul class="condition-list col-left">
        <li>Knee Pain</li>
        <li>Tendon Injuries (Patellar Tendonitis, Quad Tendon)</li>
        <li>Muscle injuries</li>
        <li>Ligament sprains or tears (MCL, LCL)</li>
        <li>Bursitis</li>
        <li>Osteoarthritis</li>
        <li class="gap">Hip Pain</li>
        <li>Muscle pain or injury</li>
        <li>Pyriformis syndrome</li>
        <li>Greater Trochanteric Bursitis</li>
        <li class="gap">Tendon Injuries</li>
        <li>Sacroiliac joint pain</li>
        <li>Hamstring tendonitis or tears</li>
        <li>Osteoarthritis</li>
      </ul>
      <ul class="condition-list col-right">
        <li>Shoulder and Arm Pain</li>
        <li>Rotator Cuff tendonitis, tendonopathy or partial tears</li>
        <li>Bicipital tendonitis</li>
        <li>Medial and Lateral epicondylitis (golfers &amp; tennis elbow)</li>
        <li>Ulnar Collateral Ligament sprain or tear</li>
        <li class="gap">Lower Leg and Foot Pain</li>
        <li>Plantar Fasciitis</li>
        <li>Shin Splints</li>
        <li>Peroneal tendonitis</li>
        <li>Ankle sprains/ligament injury</li>
        <li>Achilles tendonitis or partial tears</li>
      </ul>
    </div>
  </section>

  <section class="contact">
    <h2 class="contact-title">Contact Details</h2>
    <p class="contact-line"><svg viewBox="0 0 16 16" aria-hidden="true"><rect width="16" height="16" rx="2"/><path d="M5 3.5l1.6 2.2-1 1.2a7 7 0 0 0 3.5 3.5l1.2-1 2.2 1.6-.8 1.6C8 12.8 3.2 8 3.4 4.3z" fill="#fff"/></svg>555-0142-88</p>
    <p class="contact-line"><svg viewBox="0 0 16 16" aria-hidden="true"><rect y="3" width="16" height="10" rx="1"/><path d="M1 4l7 5 7-5" stroke="#fff" stroke-width="1.3" fill="none"/></svg>info@kelvawind.com</p>
    <p class="contact-line"><svg viewBox="0 0 16 16" aria-hidden="true"><circle cx="8" cy="8" r="7.5"/><path d="M1 8h14M8 1c-3 3.5-3 10.5 0 14M8 1c3 3.5 3 10.5 0 14" stroke="#fff" stroke-width="1" fill="none"/></svg>kelvawind.com</p>
  </section>

  <h2 class="cover-title">Platelet-Rich Plasma<br>and BMCC</h2>
</main>
</body>
</html>
```